New CV / Resume for CIO / Head IT

I would need a new fresh design for my CV, which reflects the seniority of a CIO but also looks fresh, has some IT / digital connection.

What I need...
- CV / Resume
- Cover Letter
- Netvora Background
- Logo / Business Card Design

Old CV is attached (do not include latest position) and Netvora Profile could be looked at https://www.netvora.example/in/brumelkoritz/

Please do not reuse the old design elements. I really want a new design like the ones below. Some good examples
https://plumfoundry.example/ZestyGlyph/5038214-Crisp-Profile-Layout?u=kpt
https://plumfoundry.example/tovalmint/431762-ProfileSheet?u=kpt

Target Market(s)

IT

Font styles to use
Serif
Sans Serif

Colors
0094D4
00A9DD
6FCCEA
C7EBF8
E9F6FB

```html
<!DOCTYPE html>
<html lang="en">
<head>
<meta charset="utf-8">
<title>Lukas Brenner – CV</title>
<link href="https://fonts.googleapis.com/css2?family=Lato:wght@300;400;700&display=swap" rel="stylesheet">
<style>
:root{
  --bg:#e4e6e8;
  --paper:#ffffff;
  --ink:#1b1f24;
  --dark:#121a20;
  --black:#050505;
  --blue:#0094d4;
  --sky:#c7ebf8;
  --green:#10a58a;
  --grey:#eeeeee;
  --muted:#6b7178;
  --soft:#d0d4d7;
}
*{margin:0;padding:0;box-sizing:border-box}
html,body{width:1200px;height:888px;overflow:hidden}
body{background:var(--bg);font-family:'Lato',sans-serif;color:var(--ink);position:relative}
.sheet{position:absolute;top:118px;width:506px;height:655px;background:var(--paper);overflow:hidden;box-shadow:0 6px 18px rgba(0,0,0,.18)}
.sheet--front{left:56px}
.sheet--inside{left:603px}
.shapes{position:absolute;inset:0;width:506px;height:655px}
.abs{position:absolute}

/* front */
.portrait{left:0;top:0;width:163px;height:222px;background:linear-gradient(180deg,var(--sky) 0%,#a9d9ee 45%,#3a4048 75%,#1a1d22 100%)}
.name{left:168px;top:66px;font-weight:300;color:var(--ink);line-height:1}
.name__first{font-size:36px;letter-spacing:1px}
.name__last{font-size:42px;letter-spacing:8px;margin-top:15px}
.role{left:209px;top:218px;font-size:23px;font-weight:400;line-height:30px;color:var(--ink)}
.sketch{background:linear-gradient(135deg,rgba(200,205,210,.16),rgba(200,205,210,.04))}
.sketch--top{left:330px;top:252px;width:176px;height:98px}
.sketch--bottom{left:335px;top:497px;width:171px;height:158px}
.highlights{left:14px;top:260px;width:154px;list-style:none;color:#d7dbde;font-size:11.5px;line-height:18px}
.highlights li{position:relative;padding-left:17px;text-align:justify}
.highlights li:nth-child(2){margin-top:58px}
.highlights li:nth-child(3){margin-top:59px}
.highlights svg{position:absolute;left:0;top:4px}
.contact{right:12px;top:366px;text-align:right;color:#fff;font-size:15px;line-height:25px}
.contact li{list-style:none;display:flex;justify-content:flex-end;align-items:center;gap:8px}
.contact svg{width:18px;height:18px;flex:none}

/* inside */
.head-name{left:14px;top:15px;font-size:15px;letter-spacing:.5px}
.head-name b{font-weight:400}
.head-name span{font-weight:300}
.doc-title{left:14px;top:49px;font-size:23px;font-weight:300;letter-spacing:1px;color:var(--ink)}
.head-contact{left:252px;top:10px;font-size:11.5px;line-height:14px;color:#4a4f55;font-weight:300;font-style:normal}
.section-title{font-size:15px;letter-spacing:.3px}
.section-title b{font-weight:700}
.section-title span{font-weight:300}
.personal{left:12px;top:98px}
.personal .section-title{color:var(--green)}
.details{margin-top:10px;font-size:7.5px;line-height:10px;color:#bbb}
.details b{color:#ddd;font-weight:400}
.expertise{left:12px;top:188px;color:#fff}
.skills{display:grid;grid-template-columns:150px 143px 140px;margin-top:7px;font-size:8px;line-height:10px}
.skills ul{list-style:none}
.skills li::before{content:"›";font-weight:700;margin-right:5px}
.experience-title{left:12px;top:294px;color:var(--ink)}
.job{position:absolute;left:0;width:506px}
.job__date{position:absolute;left:22px;top:0;font-size:7.5px;color:var(--muted)}
.job__body{position:absolute;left:142px;top:0;width:364px}
.job__role{font-size:7.5px;color:var(--muted)}
.job__org{font-size:8px;font-weight:700;color:var(--green);margin-top:1px}
.job__tasks{list-style:none;margin-top:6px;font-size:7.6px;line-height:10px;color:var(--ink)}
.job__tasks li::before{content:"›";color:var(--blue);font-weight:700;margin-right:6px}
</style>
</head>
<body>

<section class="sheet sheet--front" aria-label="Front page">
  <svg class="shapes" viewBox="0 0 506 655" aria-hidden="true">
    <polygon points="163,52 418,52 418,172 163,172" fill="var(--grey)"/>
    <polygon points="0,222 176,222 316,655 0,655" fill="var(--dark)"/>
    <polygon points="176,222 188,222 330,655 318,655" fill="var(--blue)"/>
    <polygon points="188,222 194,222 336,655 330,655" fill="var(--soft)"/>
    <polygon points="408,0 414,0 506,198 506,212" fill="var(--green)"/>
    <polygon points="420,0 506,0 506,186" fill="var(--blue)"/>
    <polygon points="176,352 506,352 506,493 232,493" fill="var(--green)"/>
  </svg>
  <div class="abs portrait" role="img" aria-label="Portrait photo of Lukas Brenner in a dark suit"></div>
  <div class="abs sketch sketch--top" role="img" aria-label="Faint hand-drawn IT process sketches"></div>
  <div class="abs sketch sketch--bottom" role="img" aria-label="Faint hand-drawn architecture and engineering sketches"></div>
  <h1 class="abs name"><div class="name__first">LUKAS</div><div class="name__last">BRENNER</div></h1>
  <p class="abs role">Head-IT, Manager<br>and Coach</p>
  <ul class="abs highlights">
    <li><svg width="10" height="9" viewBox="0 0 10 9"><path d="M1 5l3 3 5-7" stroke="var(--green)" stroke-width="2" fill="none"/></svg>Agile leadership and coaching experience for globally distributed teams (up to 30 employees)</li>
    <li><svg width="10" height="9" viewBox="0 0 10 9"><path d="M1 5l3 3 5-7" stroke="var(--green)" stroke-width="2" fill="none"/></svg>Profound expertise in project and cost management</li>
    <li><svg width="10" height="9" viewBox="0 0 10 9"><path d="M1 5l3 3 5-7" stroke="var(--green)" stroke-width="2" fill="none"/></svg>Many years of experience with collaboration infrastructures, engineering, and architecture</li>
  </ul>
  <ul class="abs contact">
    <li>Lindenweg 24<svg viewBox="0 0 18 18"><path d="M9 1a6 6 0 0 0-6 6c0 4.5 6 10 6 10s6-5.5 6-10a6 6 0 0 0-6-6z" fill="var(--black)"/><circle cx="9" cy="7" r="2.2" fill="var(--green)"/></svg></li>
    <li>CH-4821 Talbrunn am See<svg viewBox="0 0 18 18"></svg></li>
    <li>lukas.brenner@mailvault.example<svg viewBox="0 0 18 18"><rect x="1.5" y="4" width="15" height="10" fill="none" stroke="var(--black)" stroke-width="1.5"/><path d="M1.5 4l7.5 6 7.5-6" fill="none" stroke="var(--black)" stroke-width="1.5"/></svg></li>
    <li>+41 795550142<svg viewBox="0 0 18 18"><path d="M5 2l3 3-2 2c1 2 3 4 5 5l2-2 3 3-2 3C8 15 3 10 2 4z" fill="none" stroke="var(--black)" stroke-width="1.5"/></svg></li>
  </ul>
</section>

<section class="sheet sheet--inside" aria-label="Inside page">
  <svg class="shapes" viewBox="0 0 506 655" aria-hidden="true">
    <polygon points="0,48 212,48 232,80 0,80" fill="var(--blue)"/>
    <polygon points="0,80 390,80 420,180 0,180" fill="var(--black)"/>
    <polygon points="0,262 455,262 440,288 0,288" fill="var(--black)"/>
    <polygon points="0,178 412,178 465,262 0,262" fill="var(--green)"/>
    <polygon points="420,0 426,0 506,176 506,190" fill="var(--green)"/>
    <polygon points="432,0 506,0 506,162" fill="var(--blue)"/>
    <line x1="0" y1="318" x2="133" y2="318" stroke="var(--black)" stroke-width="2"/>
    <line x1="133" y1="318" x2="133" y2="638" stroke="var(--black)" stroke-width="2"/>
    <line x1="30" y1="644" x2="368" y2="644" stroke="var(--black)" stroke-width="2.5"/>
    <g fill="var(--green)"><circle cx="133" cy="333" r="3.5"/><circle cx="133" cy="441" r="3.5"/><circle cx="133" cy="556" r="3.5"/></g>
  </svg>
  <p class="abs head-name"><span>LUKAS</span> <b>BRENNER</b></p>
  <h1 class="abs doc-title">LEBENSLAUF</h1>
  <address class="abs head-contact">Lindenweg 24<br>CH-4821 Talbrunn am See<br>lukas.brenner@mailvault.example<br>+41 795550142</address>

  <div class="abs personal">
    <h2 class="section-title"><b>PERSONAL</b> <span>DETAILS</span></h2>
    <div class="details">
      <div><b>Birthday / -place</b> 14.07.1984 in Ravensmoor (Germany)</div>
      <div><b>Nationality</b> German</div>
      <div><b>Marital Status</b> Married (2017 Korlin)</div>
      <div><b>Children</b> Two girls</div>
    </div>
  </div>

  <div class="abs expertise">
    <h2 class="section-title"><b>AREAS OF EXPERTISE</b> <span>&amp; EXPERIENCE</span></h2>
    <div class="skills">
      <ul><li>Agile Leadership</li><li>Service Design &amp; Transition</li><li>Coaching</li><li>Nimbus 365</li></ul>
      <ul><li>Design &amp; Engineering</li><li>Project Management</li><li>ShellForge Scripting</li><li>Migration &amp; Architecture</li></ul>
      <ul><li>IT Consulting &amp; Support</li><li>Personnel Training</li><li>Experience Abroad</li><li>Change Management</li></ul>
    </div>
  </div>

  <h2 class="abs section-title experience-title"><b>PROFESSIONAL</b> <span>EXPERIENCE</span></h2>

  <article class="job" style="top:329px">
    <div class="job__date">since 12.2018</div>
    <div class="job__body">
      <div class="job__role">Head IT Alpora Schweiz &amp; Head ICT Cluster Central Europe</div>
      <div class="job__org">Alpora AG / Nordhain Werke GmbH &amp; Co. KGaA</div>
      <ul class="job__tasks">
        <li>Operational and personnel responsibility for the IT organization in Switzerland</li>
        <li>Operational and personnel responsibility for the ICT organization in Germany</li>
        <li>Support of the global export organization and HQ</li>
        <li>Planning, organization and development of IT infrastructure and application</li>
        <li>Operation of the Service Desk Organization in Switzerland &amp; Germany</li>
        <li>Coordination and implementation with the Group IT strategy</li>
        <li>IT Change and Project Management</li>
      </ul>
    </div>
  </article>

  <article class="job" style="top:437px">
    <div class="job__date">07.2017 - 11.2018</div>
    <div class="job__body">
      <div class="job__role">Manager and Coach of DWP Platform Engineering &amp; Operations</div>
      <div class="job__org">Helvara Management Ltd (Switzerland)</div>
      <ul class="job__tasks">
        <li>People management for 31 employees (MBO, hiring, escalations, etc.)</li>
        <li>Personal development coaching (systemic)</li>
        <li>Drive change management and cultural development</li>
        <li>Organization transformation to adopt agile principles</li>
        <li>Shape and support the Digital Workplace strategy</li>
        <li>Support sourcing activities</li>
        <li>Drive and support the strategic planning of our global platforms<br>&nbsp;&nbsp;&nbsp;(Postline, ShareDock &amp; Talkwave / UC)</li>
      </ul>
    </div>
  </article>

  <article class="job" style="top:552px">
    <div class="job__date">05.2014 - 06.2017</div>
    <div class="job__body">
      <div class="job__role">Expert ShareDock Engineer &amp; Project Manager</div>
      <div class="job__org">Helvara Management Ltd (Switzerland)</div>
      <ul class="job__tasks">
        <li>Project Manager of the ShareDock 2016 &amp; Hybrid project</li>
        <li>Defining and Engineering Nimbus Office / ShareDock online implementation</li>
        <li>Technical responsibility for the ShareDock infrastructure</li>
        <li>Project lead for ShareDock 2016 migration and the preparation of a Nimbus Office-based hybrid solution</li>
        <li>Support and consulting for introduction projects for Nimbus Business Intelligence, ShareDock for<br>&nbsp;&nbsp;&nbsp;mobile devices, taxonomy and access management during development and implementation phases</li>
      </ul>
    </div>
  </article>
</section>

</body>
</html>
```